Postcard Design

Velvet Petal a Waxing Boutique - We need a postcard Front of it with a boarder done as a dainty picture frame and inside listing our services menu. We would like the picture frame to be white and the background to be a light grey and service menu writing in white as well. On back we need name, address, etc. We weould like the name to be in Turquise. Do you help design logos?
menu sheet -
Facial Services:
Brow Shaping $18
Lip - $12
Brow and Lip Combo $25
Sideburns - $12
Nose $10
Ears $10
Full Face Combo Excluding Brows $40
Full Face Combo w/ Brow Shaping $55
Lash Tint $20
Brow Tint $15
(This is to darken brows only)
Brow Shaping + Brow Tint $33

BODY WAXING :
Neck $15
Shoulders$20
Full back $45
Chest $45
(Abdomen Included)
Abdomen $15
Underarms $15
Full Arm $40
Half Arm $30
Full Leg $60
(Bikini line not included, This covers the upper thigh down to the feet and toes)
Half Leg $45
(Upper or Lower leg)
Modest Bikini - $35 Female Only
Brazilian Bikini $55 Female Only
Buttocks $20

Whats So Special About Our Pricing? Its Simple:
*Straight Forward Prices and No Tipping Policy!

Back of Card -

Velvet Petal
{Waxing Boutique}

Located in Studios Marigo
415 W. Corbin Dale Blvd
Suite 17
Rockwall, TX 75849
(972)514-2078

```html
<!DOCTYPE html>
<html lang="en">
<head>
<meta charset="utf-8">
<title>Velvet Petal Waxing Boutique – Services Menu</title>
<link rel="stylesheet" href="https://fonts.googleapis.com/css2?family=Dancing+Script:wght@400;500&family=Open+Sans:ital,wght@1,400;1,700&family=Questrial&display=swap">
<style>
  :root {
    --card-grey: #a7a7a9;
    --frame-white: #ffffff;
    --frame-light: #e4e4e6;
    --frame-shade: #d6d6d8;
    --ink-white: #ffffff;
    --ink-slate: #5a5a5c;
    --band-dark: rgba(72, 72, 74, 0.62);
  }
  html, body {
    margin: 0;
    padding: 0;
    width: 1200px;
    height: 929px;
    overflow: hidden;
    background: var(--card-grey);
  }
  .postcard {
    position: relative;
    width: 1200px;
    height: 929px;
    background: var(--card-grey);
    overflow: hidden;
    font-family: "Open Sans", Arial, sans-serif;
    color: var(--ink-white);
  }
  .lace-frame {
    position: absolute;
    inset: 0;
  }
  .frame-lines {
    position: absolute;
    inset: 0;
    pointer-events: none;
  }
  .brand-name {
    position: absolute;
    top: 138px;
    left: 0;
    width: 1200px;
    margin: 0;
    text-align: center;
    font-family: "Dancing Script", cursive;
    font-weight: 500;
    font-size: 132px;
    line-height: 1;
    color: var(--ink-white);
  }
  .brand-tagline {
    position: absolute;
    top: 282px;
    left: 0;
    width: 1200px;
    margin: 0;
    padding-left: 0.97em;
    box-sizing: border-box;
    text-align: center;
    font-family: "Questrial", Arial, sans-serif;
    font-weight: 400;
    font-size: 34px;
    letter-spacing: 0.97em;
    line-height: 1;
    color: var(--ink-slate);
  }
  .title-rule {
    position: absolute;
    top: 330px;
    left: 165px;
    width: 870px;
    height: 1.5px;
    background: var(--ink-white);
  }
  .menu-column {
    position: absolute;
    top: 350px;
    white-space: nowrap;
  }
  .menu-column--facial { left: 233px; }
  .menu-column--body { left: 657px; }
  .menu-heading {
    margin: 0 0 10px;
    font-family: "Dancing Script", cursive;
    font-weight: 400;
    font-size: 31px;
    line-height: 1.2;
  }
  .service-list {
    list-style: none;
    margin: 0;
    padding: 0;
    font-style: italic;
    font-size: 18.3px;
    letter-spacing: -0.2px;
    line-height: 25px;
  }
  .service-price { font-weight: 700; }
  .pricing-band {
    position: absolute;
    top: 838px;
    left: 0;
    width: 1200px;
    height: 56px;
    background: var(--band-dark);
    display: flex;
    align-items: center;
    justify-content: center;
  }
  .pricing-promise {
    margin: 0;
    font-style: italic;
    font-size: 31px;
    color: var(--ink-white);
  }
</style>
</head>
<body>
<main class="postcard">
  <svg class="lace-frame" width="1200" height="929" viewBox="0 0 1200 929" role="img" aria-label="Dainty white lace picture frame with swirling floral scrollwork around the card edges">
    <defs>
      <linearGradient id="lace-tone" x1="0" y1="0" x2="1" y2="1">
        <stop offset="0" stop-color="var(--frame-light)"/>
        <stop offset="1" stop-color="var(--frame-shade)"/>
      </linearGradient>
    </defs>
    <path fill="url(#lace-tone)" fill-rule="evenodd"
      d="M0 0H1200V929H0Z
         M300 105H900C1010 105 1085 190 1085 300V610C1085 715 1010 790 900 790H300C190 790 130 715 130 610V300C130 190 190 105 300 105Z"/>
  </svg>

  <svg class="frame-lines" width="1200" height="929" viewBox="0 0 1200 929" aria-hidden="true">
    <path fill="none" stroke="var(--frame-white)" stroke-width="4"
      d="M300 105H900C1010 105 1085 190 1085 300V610C1085 715 1010 790 900 790H300C190 790 130 715 130 610V300C130 190 190 105 300 105Z"/>
    <path fill="none" stroke="var(--frame-white)" stroke-width="1.2"
      d="M300 92H900C1018 92 1098 182 1098 300V610C1098 723 1018 803 900 803H300C182 803 117 723 117 610V300C117 182 182 92 300 92Z"/>
    <path fill="none" stroke="var(--frame-white)" stroke-width="1.2"
      d="M300 80H900C1026 80 1110 174 1110 300V610C1110 731 1026 815 900 815H300C174 815 105 731 105 610V300C105 174 174 80 300 80Z"/>
  </svg>

  <h1 class="brand-name">Velvet Petal</h1>
  <p class="brand-tagline">WAXING BOUTIQUE</p>
  <div class="title-rule"></div>

  <section class="menu-column menu-column--facial">
    <h2 class="menu-heading">Facial Services</h2>
    <ul class="service-list">
      <li>Brow Shaping...<span class="service-price">$18</span></li>
      <li>Lip...<span class="service-price">$12</span></li>
      <li>Brow and Lip Combo...<span class="service-price">$25</span></li>
      <li>Sideburns...<span class="service-price">$12</span></li>
      <li>Nose...<span class="service-price">$10</span></li>
      <li>Ears...<span class="service-price">$10</span></li>
      <li>Full Face Combo Excluding Brows...<span class="service-price">$40</span></li>
      <li>Full Face Combo with Brow Shaping...<span class="service-price">$55</span></li>
      <li>Lash Tint...<span class="service-price">$20</span></li>
      <li>Brow Tint...<span class="service-price">$15</span> (This is to darken brows only)</li>
      <li>Brow Shaping and Brow Tint...<span class="service-price">$33</span></li>
    </ul>
  </section>

  <section class="menu-column menu-column--body">
    <h2 class="menu-heading">Body Waxing</h2>
    <ul class="service-list">
      <li>Neck...<span class="service-price">$15</span></li>
      <li>Shoulders...<span class="service-price">$20</span></li>
      <li>Full back...<span class="service-price">$45</span></li>
      <li>Chest...<span class="service-price">$45</span> (Abdomen included)</li>
      <li>Abdomen...<span class="service-price">$15</span></li>
      <li>Underarms...<span class="service-price">$15</span></li>
      <li>Full Arm...<span class="service-price">$40</span></li>
      <li>Half Arm...<span class="service-price">$30</span></li>
      <li>Full Leg...<span class="service-price">$60</span> (Bikini line not included. This covers<br>the upper thigh down to the feet and toes)</li>
      <li>Half Leg...<span class="service-price">$45</span> (Upper or lower leg)</li>
      <li>Modest Bikini...<span class="service-price">$35</span> (Female only)</li>
      <li>Brazilian Bikini...<span class="service-price">$55</span> (Female only)</li>
      <li>Buttocks...<span class="service-price">$20</span></li>
    </ul>
  </section>

  <div class="pricing-band">
    <p class="pricing-promise">“ Straight forward prices and a no tipping policy...! ”</p>
  </div>
</main>
</body>
</html>
```